Maplerise Trading Inc. needs an innovative idea for letterhead and visiting cards.

Maplerise Trading Inc. is a Canadian brand since 2007. It is a renown dealer of kids and office furniture locally. Moreover, exporting electric fixtures e.g. switches, LED's, down-lights etc. to Middle East and Africa. We have initiated a number of steps including re-branding, to boost our export in 2020. We have successfully designed our new logo a few months ago through 'Artfolio' and now we are looking for an innovative idea for a letterhead.
Some key points:
• Red, black and white are the three colors used in all our packaging and furniture. (grey is optional)
• Shouldn’t be too wide.
• Use of watermark is preferable.
• You can visit our North American site at www.mapleriseinc.com. Export website of the company will be launched soon. www.mapleriseinc.ca
• Same letterhead will be used locally and internationally.
• Our new logo and sample packaging is attached.

```html
<!DOCTYPE html>
<html lang="en">
<head>
<meta charset="utf-8">
<title>Maplerise Trading Inc. — Letterhead</title>
<link href="https://fonts.googleapis.com/css2?family=Roboto+Condensed:wght@300;400&display=swap" rel="stylesheet">
<style>
  :root {
    --brand-red: #a11015;
    --ink-grey: #555555;
    --paper: #f4f4f4;
    --backdrop: #e6e6e6;
    --white: #ffffff;
  }
  * { box-sizing: border-box; margin: 0; padding: 0; }
  html, body {
    width: 1200px;
    height: 800px;
    overflow: hidden;
    background: var(--backdrop);
    font-family: "Roboto Condensed", Arial, sans-serif;
  }
  .canvas {
    width: 1200px;
    height: 800px;
    display: flex;
    align-items: center;
    justify-content: center;
  }
  .letterhead {
    position: relative;
    width: 540px;
    height: 720px;
    background: var(--paper);
    box-shadow: 0 2px 10px rgba(0,0,0,0.12);
    overflow: hidden;
  }
  .top-accent {
    position: absolute;
    top: 0;
    left: 260px;
    width: 120px;
    height: 58px;
    background: var(--brand-red);
  }
  .brand {
    position: absolute;
    top: 66px;
    left: 40px;
    display: flex;
    align-items: center;
    gap: 10px;
  }
  .brand-square {
    width: 30px;
    height: 30px;
    background: var(--brand-red);
  }
  .brand-name {
    font-weight: 300;
    font-size: 24px;
    line-height: 1;
    letter-spacing: 1.5px;
    text-transform: uppercase;
    color: var(--ink-grey);
  }
  .footer {
    position: absolute;
    left: 0;
    right: 0;
    bottom: 34px;
    display: flex;
    align-items: flex-end;
    justify-content: space-between;
  }
  .address {
    padding-left: 40px;
    font-size: 11px;
    line-height: 1.35;
    color: var(--ink-grey);
  }
  .contact-band {
    display: flex;
    align-items: center;
    gap: 14px;
    height: 20px;
    padding: 0 14px;
    background: var(--brand-red);
    color: var(--white);
    font-size: 10px;
    letter-spacing: 0.2px;
  }
  .contact-item {
    display: flex;
    align-items: center;
    gap: 4px;
    white-space: nowrap;
  }
  .contact-item svg {
    width: 9px;
    height: 9px;
    fill: var(--white);
  }
</style>
</head>
<body>
<main class="canvas">
  <article class="letterhead">
    <div class="top-accent" role="img" aria-label="Red leaf accent at the top edge"></div>

    <header class="brand">
      <span class="brand-square"></span>
      <span class="brand-name">Maplerise Trading</span>
    </header>

    <footer class="footer">
      <address class="address">
        48 Cedarline Rd, Unit 210<br>
        Markham Falls, ON L3R 2K8
      </address>
      <div class="contact-band">
        <span class="contact-item">
          <svg viewBox="0 0 10 10" aria-hidden="true"><path d="M2 0.5 L3.6 0.5 L4.3 2.6 L3.2 3.5 Q4.2 5.8 6.5 6.8 L7.4 5.7 L9.5 6.4 L9.5 8 Q9.5 9.5 8 9.5 Q0.5 8.8 0.5 2 Q0.5 0.5 2 0.5 Z"/></svg>
          +1 (800) 555-0142
        </span>
        <span class="contact-item">
          <svg viewBox="0 0 10 10" aria-hidden="true"><path d="M0.5 2 L9.5 2 L9.5 8.5 L0.5 8.5 Z M1 2.4 L5 5.6 L9 2.4" stroke="#a11015" stroke-width="0.8"/></svg>
          info@mapleriseinc.com
        </span>
        <span class="contact-item">
          <svg viewBox="0 0 10 10" aria-hidden="true"><circle cx="5" cy="5" r="4.5"/></svg>
          www.mapleriseinc.com
        </span>
      </div>
    </footer>
  </article>
</main>
</body>
</html>
```